Business card needed for the Rydo of Dry Cleaning!

We need a slick business card design for a new company based out of Montreal called Casiers Plimo&Zet inc. (in French) and Plimo&Zet Lockers inc. (in English). We're the Rydo of Laundry. We offer services of dry cleaning, laundry (wash&fold), minor clothing alterations, shoe repair and parcel delivery through 24/7 secured and connected lockers. Ordres are placed through our mobile application. Real time notification are sent to customers when their order is ready for pickup. The lockers will be placed throughout the downtown area, in condo and office towers, where a high density of busy people converge. It is simple, user-friendly, and most importantly convenient. We're the out of the box dry cleaner, literally.

Target Market(s)

1) Professional workers wearing suits daily
2) Campus students living in residences
3) People using laundromats
4) Families with children/yuppies who prefer to use their time doing something else than laundry

Industry/Entity Type

Dry Cleaning

Contact Information for Business Card

Name / Annick-Solène Trudel
Title / CEO & Founder
Company Name / Casiers Plimo&Zet inc. | Plimo&Zet Lockers inc.
Website www.plimozet.ca

Requirements
Must have
• Text Logo: Plimo&Zet - Nettoyeurs 24/7 Cleaners
• Logo on one side and contact info on the other (bilingual)
• Minimalist, pure design
• "We care" for your belongings feeling
• Professional, technological, clean & fresh look
Should not have
• No busy visuals. No rainbow colors.

```html
<!DOCTYPE html>
<html lang="fr">
<head>
<meta charset="utf-8">
<title>Plimo&amp;Zet – Carte d'affaires</title>
<link rel="stylesheet" href="https://fonts.googleapis.com/css2?family=Source+Sans+3:wght@300;400;600;700&display=swap">
<style>
  :root {
    --backdrop: #3b3b3b;
    --card: #0f0f10;
    --ink: #f4f4f4;
    --ink-soft: #d6d6d6;
    --rule: #cfcfcf;
  }
  * { box-sizing: border-box; margin: 0; padding: 0; }
  html, body {
    width: 1200px; height: 720px; overflow: hidden;
    background: var(--backdrop);
    font-family: "Source Sans 3", "Segoe UI", sans-serif;
    color: var(--ink);
  }
  .sheet {
    position: relative; width: 1200px; height: 720px;
    display: flex; align-items: center; justify-content: center; gap: 50px;
  }
  .card {
    position: relative;
    width: 500px; height: 286px;
    background: var(--card);
    border-radius: 6px;
    box-shadow: 0 10px 30px rgba(0,0,0,.35);
    overflow: hidden;
  }

  /* Front: brand */
  .brand {
    position: absolute; left: 70px; top: 92px;
  }
  .brand-name {
    font-weight: 300; font-size: 54px; line-height: 1;
    letter-spacing: 1px; text-transform: uppercase;
  }
  .brand-tagline {
    margin-top: 6px;
    font-weight: 400; font-size: 14px; letter-spacing: 1.2px;
    text-transform: uppercase; color: var(--ink-soft);
  }
  .brand-hours {
    margin-top: 4px; margin-left: 170px;
    font-weight: 400; font-size: 14px; letter-spacing: 1.2px;
    color: var(--ink-soft);
  }

  /* Back: contact */
  .identity {
    position: absolute; right: 272px; top: 92px; text-align: right;
  }
  .identity-name {
    font-weight: 700; font-size: 15px; letter-spacing: .3px;
    text-transform: uppercase; white-space: nowrap;
  }
  .identity-title {
    margin-top: 2px; font-size: 14px; font-weight: 400; color: var(--ink-soft);
  }
  .divider {
    position: absolute; left: 246px; top: 88px;
    width: 1px; height: 92px; background: var(--rule);
  }
  .contacts {
    position: absolute; left: 264px; top: 100px;
    list-style: none; display: flex; flex-direction: column; gap: 8px;
  }
  .contacts li {
    display: flex; align-items: center; gap: 10px;
    font-size: 15px; font-weight: 400; white-space: nowrap;
  }
  .contacts svg { width: 13px; height: 13px; fill: var(--ink); flex: none; }
  .motto {
    position: absolute; left: 0; right: 0; top: 212px;
    text-align: center; font-size: 15px; font-weight: 400;
  }
</style>
</head>
<body>
<main class="sheet">
  <section class="card card-front" aria-label="Recto">
    <div class="brand">
      <div class="brand-name">Plimo&amp;Zet</div>
      <div class="brand-tagline">Nettoyeurs • Cleaners</div>
      <div class="brand-hours">24/7</div>
    </div>
  </section>

  <section class="card card-back" aria-label="Verso">
    <div class="identity">
      <div class="identity-name">Annick-Solène Trudel</div>
      <div class="identity-title">CEO &amp; Founder</div>
    </div>
    <div class="divider"></div>
    <ul class="contacts">
      <li>
        <svg viewBox="0 0 16 16" aria-hidden="true"><path d="M3 1.5c.6-.4 1.4-.3 1.8.3l1.6 2.3c.4.6.3 1.3-.2 1.7l-1 .8c.8 1.7 2.1 3 3.8 3.8l.8-1c.4-.5 1.2-.6 1.7-.2l2.3 1.6c.6.4.7 1.2.3 1.8l-.9 1.3c-.6.8-1.7 1.1-2.6.7C6.2 13.2 2.8 9.8 1.4 5.6c-.3-.9 0-2 .7-2.6z"/></svg>
        <span>514 555 0172</span>
      </li>
      <li>
        <svg viewBox="0 0 16 16" aria-hidden="true"><path d="M1 3h14v10H1z M2.2 4.2 8 8.6l5.8-4.4z" fill-rule="evenodd"/></svg>
        <span>info@plimozet.com</span>
      </li>
      <li>
        <svg viewBox="0 0 16 16" aria-hidden="true"><path d="M8 1a7 7 0 1 0 0 14A7 7 0 0 0 8 1zm0 1.5c.7 0 1.6 1.5 1.9 4H6.1C6.4 4 7.3 2.5 8 2.5zM2.6 6.5h2c-.1 1 0 2 0 3h-2a5.5 5.5 0 0 1 0-3zm3.5 3c-.1-1-.1-2 0-3h3.8c.1 1 .1 2 0 3zm5.3 0c.1-1 .1-2 0-3h2a5.5 5.5 0 0 1 0 3zM6.1 11h3.8c-.3 2.5-1.2 4-1.9 4s-1.6-1.5-1.9-4z"/></svg>
        <span>www.plimozet.ca</span>
      </li>
    </ul>
    <p class="motto">"We care" for your belongings feeling</p>
  </section>
</main>
</body>
</html>
```